Vision, Mission and Culture Posters

We have written text paragraphs for our company vision and mission and need them made into a2 or a3 sized posters using our logo for inspiration for colour. Our company culture has 10 paragraphs and we'd like this to be a single poster of a2 or a1. Each poster should have the logo on and share common design. It's not a complex job really.

Industry/Entity Type

It Company

Requirements
Nice to have
• These will be going up on our office wall so need to be clear to read from a distance and look professional but also not stodgy.

```html
<!DOCTYPE html>
<html lang="en">
<head>
<meta charset="utf-8">
<title>Vision and Mission Poster</title>
<link href="https://fonts.googleapis.com/css2?family=Source+Sans+3:wght@400;700&display=swap" rel="stylesheet">
<style>
  :root {
    --photo-dark: #1c1a1d;
    --photo-mid: #6b6468;
    --photo-light: #d9d6d4;
    --vision-red: #b0242a;
    --vision-red-light: #cf3a36;
    --mission-orange: #f07a22;
    --mission-orange-light: #f59a55;
    --footer-light: #f1f1f1;
    --footer-grey: #bdbdbd;
    --brand-yellow: #ffe600;
    --ink: #111111;
    --white: #ffffff;
  }
  * { margin: 0; padding: 0; box-sizing: border-box; }
  html, body { width: 848px; height: 1200px; overflow: hidden; }
  body { font-family: "Source Sans 3", "Source Sans Pro", Arial, sans-serif; background: var(--white); }

  .poster { position: relative; width: 848px; height: 1200px; overflow: hidden; }

  .hero-photo {
    position: absolute; left: 0; top: 0; width: 848px; height: 481px;
    background:
      radial-gradient(ellipse 60% 45% at 50% 20%, var(--photo-light) 0%, rgba(217,214,212,0) 70%),
      linear-gradient(180deg, var(--photo-mid) 0%, #3a3538 45%, var(--photo-dark) 100%);
  }

  .statement { position: absolute; left: 0; width: 848px; padding: 0 68px 0 70px; }
  .statement h2 { font-size: 27px; font-weight: 700; line-height: 1; margin-bottom: 10px; }
  .statement p { font-size: 17.5px; line-height: 24px; text-align: justify; }

  .vision {
    top: 481px; height: 141px; padding-top: 29px;
    background: radial-gradient(ellipse 60% 90% at 50% 40%, var(--vision-red-light) 0%, var(--vision-red) 100%);
    color: var(--white);
  }
  .vision h2 { margin-bottom: 13px; }

  .mission {
    top: 622px; height: 257px; padding-top: 30px;
    background: radial-gradient(ellipse 60% 80% at 50% 40%, var(--mission-orange-light) 0%, var(--mission-orange) 100%);
    color: var(--ink);
  }
  .mission h2 { margin-bottom: 8px; }

  .brand-footer {
    position: absolute; left: 0; top: 879px; width: 848px; height: 321px;
    background: radial-gradient(ellipse 70% 70% at 50% 35%, var(--footer-light) 0%, var(--footer-grey) 100%);
    display: flex; align-items: center; justify-content: center; gap: 28px;
  }
  .brand-mark { width: 70px; height: 70px; background: var(--brand-yellow); }
  .brand-name { font-size: 66px; font-weight: 700; color: var(--ink); letter-spacing: 1px; }
</style>
</head>
<body>
  <main class="poster">
    <div class="hero-photo" role="img" aria-label="Photograph of an indoor car park with rows of parked cars and painted direction arrows on the floor"></div>

    <section class="statement vision">
      <h2>Our Vission</h2>
      <p>To provide the most hassle-free parking rental service whilst giving a personal customer experience people want to tell their friends about</p>
    </section>

    <section class="statement mission">
      <h2>Our Mission</h2>
      <p>Our mission is to achieve great customer satisfaction in everything we do and offer for meeting our customers’ parking needs. We believe our path to achieving this comes through giving a simple yet thorough and friendly service to our customers without unnecessary complication. We will achieve this through using the technology available to us, continual staff training and development, regular refinement of our practices and processes along with commitment to our roles and the foundations for building our success.</p>
    </section>

    <footer class="brand-footer">
      <span class="brand-mark" aria-hidden="true"></span>
      <span class="brand-name">Bayline Parking</span>
    </footer>
  </main>
</body>
</html>
```